Historic Church website

We want our church website to feel warm, historic, and clean, modern, and easy to navigate. Dont use the anchor

Current website: https://www.meadowlarkfellowship.org/

Requirements
Should not have
• I would like to use the logo without the anchor

```html
<!DOCTYPE html>
<html lang="en">
<head>
<meta charset="utf-8">
<title>Meadowlark Fellowship Church</title>
<link rel="stylesheet" href="https://fonts.googleapis.com/css2?family=Poppins:wght@400;500;600;700&family=Oswald:wght@500;700&family=Kaushan+Script&display=swap">
<style>
:root{
  --navy:#0b1b4d;
  --navy-deep:#07133a;
  --blue:#2f7cc4;
  --blue-soft:#4a8fd0;
  --ink:#222a3a;
  --muted:#555c68;
  --paper:#ffffff;
  --mist:#eef2f7;
}
*{box-sizing:border-box;margin:0;padding:0}
html,body{width:1200px;height:4976px;overflow:hidden}
body{position:relative;background:var(--paper);font-family:'Poppins',sans-serif;color:var(--ink)}
.abs{position:absolute}
.btn{display:inline-block;background:var(--navy);color:#fff;font:600 15px 'Poppins',sans-serif;letter-spacing:.5px;border-radius:30px;padding:16px 36px;text-transform:uppercase}
.btn-sm{font-size:11px;padding:8px 18px}
.script{font-family:'Kaushan Script',cursive;color:var(--navy)}
.eyebrow{color:var(--blue);font:500 16px 'Poppins',sans-serif;letter-spacing:1px;text-transform:uppercase}

/* header */
.site-header{top:0;left:0;width:1200px;height:120px;background:var(--navy);display:flex;align-items:center;padding:0 40px;z-index:5}
.brand{display:flex;align-items:center;gap:12px;color:#fff;font:600 22px 'Poppins',sans-serif;line-height:1.1}
.brand-dot{width:36px;height:36px;border-radius:50%;background:var(--blue)}
.main-nav{margin-left:auto;display:flex;gap:34px;align-items:center;color:#fff;font:500 14px 'Poppins',sans-serif;text-transform:uppercase}
.main-nav .active{color:var(--blue-soft)}
.nav-donate{background:var(--blue);border-radius:24px;padding:10px 24px}

/* hero */
.hero{top:120px;left:0;width:1200px;height:880px;background:linear-gradient(160deg,#b99a7c 0%,#d8c3aa 40%,#8a6d56 75%,#5e4a3c 100%)}
.hero-ring{left:370px;top:320px;width:460px;height:460px;border-radius:50%;background:rgba(47,124,196,.72);display:flex;flex-direction:column;align-items:center;justify-content:center;text-align:center;color:#fff}
.hero-kicker{font:600 22px 'Poppins',sans-serif;letter-spacing:2px}
.hero-title{font:700 60px/1 'Oswald',sans-serif;text-transform:uppercase;margin:14px 0}
.hero-tag{font:400 16px 'Poppins',sans-serif;letter-spacing:1px;margin-bottom:28px}

/* about */
.about-photo{top:1000px;left:0;width:1200px;height:660px;background:linear-gradient(90deg,#d9b27a 0%,#f0cf9a 30%,#e7d8c4 60%,#cfd3d8 100%)}
.about-panel{top:1120px;left:580px;width:620px;height:520px;background:rgba(255,255,255,.92);padding:50px 40px}
.about-panel h2{font-size:64px;font-weight:400}
.rule{display:inline-block;width:90px;height:2px;background:var(--blue);vertical-align:middle;margin-left:12px}
.about-panel .lead{margin:26px 0 12px;font:600 17px/1.55 'Poppins',sans-serif;color:var(--ink)}
.about-panel p.body{font:400 12px/1.75 'Poppins',sans-serif;color:var(--muted)}

/* ministry */
.ministry{top:1700px;left:60px;width:660px}
.ministry h2{font-size:80px;font-weight:400;line-height:1}
.ministry .lead{font:600 22px/1.45 'Poppins',sans-serif;color:var(--navy);margin:26px 0 18px}
.ministry p.body{font:400 13px/1.75 'Poppins',sans-serif;color:var(--muted)}
.ministry .ref{font:italic 12px 'Poppins',sans-serif;color:var(--blue);margin-top:4px}
.ministry-emblem{top:1700px;left:770px;width:380px;height:380px;border-radius:50%;background:radial-gradient(circle,#cfe0f2 0%,#8fb5dc 70%,#5c8fc4 100%)}

/* ministries grid */
.card{top:2320px;width:360px;text-align:center}
.card-photo{width:300px;height:300px;margin:0 auto;border-radius:50%;border:8px solid var(--blue-soft)}
.card h3{font:600 24px 'Poppins',sans-serif;color:var(--navy);margin:26px 0 14px;text-transform:uppercase}
.card p{font:400 13px/1.6 'Poppins',sans-serif;color:var(--muted);padding:0 30px;min-height:84px}

/* bible studies */
.studies-photo{top:2960px;left:0;width:1200px;height:720px;background:linear-gradient(90deg,#6a4f35 0%,#b69670 25%,#ece4da 55%,#ffffff 80%)}
.studies{top:3000px;left:512px;width:640px}
.studies h2{font-size:64px;font-weight:400}
.studies .intro{font:400 14px/1.6 'Poppins',sans-serif;color:var(--muted);margin:18px 0 20px;padding-left:40px}
.event{display:flex;background:#fff;box-shadow:0 2px 10px rgba(0,0,0,.15);margin-bottom:24px;height:150px}
.event-date{width:86px;background:var(--navy);color:#fff;text-align:center;padding-top:24px;font:600 16px 'Poppins',sans-serif;line-height:1.1}
.event-date b{display:block;font-size:38px;margin:4px 0}
.event-info{flex:1;padding:18px 22px}
.event-info h4{font:600 22px 'Poppins',sans-serif;color:var(--navy)}
.event-info .when{font:500 13px 'Poppins',sans-serif;color:var(--blue);margin:4px 0 6px}
.event-info p{font:400 13px/1.5 'Poppins',sans-serif;color:var(--muted)}
.event-action{display:flex;align-items:center;padding-right:20px}

/* hope */
.hope-bg{top:3720px;left:0;width:1200px;height:540px;background:linear-gradient(90deg,#ffffff 0%,#f4f2ef 40%,#d9cfc2 80%,#c7b9a6 100%)}
.hope{top:3840px;left:0;width:1200px;text-align:center}
.hope h2{font:600 40px/1.35 'Poppins',sans-serif;color:var(--navy);text-transform:uppercase}
.hope .eyebrow{font-size:24px;margin:40px 0 20px}

/* newsletter */
.newsletter{top:4260px;left:0;width:1200px;height:280px;background:var(--blue);text-align:center;padding-top:50px}
.newsletter h2{font:400 42px 'Kaushan Script',cursive;color:#fff}
.signup{margin:40px auto 0;width:820px;height:64px;background:#fff;border-radius:32px;display:flex;align-items:center;padding:0 10px 0 40px;font:400 15px 'Poppins',sans-serif;color:var(--muted)}
.signup .btn{margin-left:auto;background:var(--blue);font-size:14px;padding:12px 34px}

/* footer */
.footer{top:4540px;left:0;width:1200px;height:360px;background:#fff}
.footer-brand{top:40px;left:0;width:1200px;display:flex;justify-content:center;align-items:center;gap:16px;font:600 38px 'Poppins',sans-serif;color:var(--navy)}
.footer-brand .brand-dot{width:56px;height:56px}
.contacts{top:250px;left:200px;width:880px;display:flex;justify-content:space-between}
.contact{display:flex;gap:14px;align-items:center;font:400 13px/1.5 'Poppins',sans-serif;color:var(--muted)}
.icon{width:40px;height:40px;border-radius:50%;background:var(--navy);display:flex;align-items:center;justify-content:center;flex:none}
.socials{top:256px;left:960px;display:flex;gap:10px}
.social{width:30px;height:30px;border-radius:50%;background:var(--blue)}
.bottom-bar{top:4900px;left:0;width:1200px;height:76px;background:var(--navy);color:#fff;font:400 11px 'Poppins',sans-serif;padding:12px 40px}
.bottom-bar .links{letter-spacing:.3px}
.bottom-bar .legal{margin-top:12px;opacity:.85}
.bottom-bar .socials{top:24px;left:1030px}
</style>
</head>
<body>

<header class="site-header abs">
  <div class="brand"><span class="brand-dot"></span><span>Meadowlark<br>Fellowship Church</span></div>
  <nav class="main-nav">
    <span class="active">Home</span><span>About MFC ▾</span><span>Ministries ▾</span><span>Bible Studies ▾</span><span>Sermon Library</span><span class="nav-donate">Donate</span>
  </nav>
</header>

<section class="hero abs" role="img" aria-label="Photo of many hands joined in prayer over an open Bible, one holding a rosary"></section>
<div class="hero-ring abs">
  <div class="hero-kicker">WELCOME TO</div>
  <div class="hero-title">Meadowlark<br>Fellowship Church</div>
  <div class="hero-tag">ANCIENT CHURCH. ANCIENT FAITH. ETERNAL TRUTH</div>
  <span class="btn">Join Our Community</span>
</div>

<section class="about-photo abs" role="img" aria-label="Photo of a wooden cross on a hill at sunset"></section>
<div class="about-panel abs">
  <h2 class="script">About Us</h2>
  <div class="eyebrow">Who we are <span class="rule"></span></div>
  <p class="lead">Meadowlark Fellowship Church is an independent Christian church in the Protestant tradition.</p>
  <p class="body">Its central tenets are found in its articles of faith and include belief in the Deity and Lordship of Jesus Christ, the Trinity, Jesus' perfect life, atoning death on the cross, bodily resurrection, and ascension; Jesus' literal return; the inerrancy of the Bible in its original manuscripts; and our need for salvation through personal faith in Jesus Christ. In keeping with the prevailing perspective of the church during the centuries immediately following the Apostles, we teach Premillennialism. That is, the belief that Messiah will physically and literally return to earth at Jerusalem before the millennial age commences.</p>
  <span class="btn" style="margin-top:34px;background:var(--blue)">Know More</span>
</div>

<section class="ministry abs">
  <h2 class="script">Ministry</h2>
  <div class="eyebrow">Meadowlark Fellowship Church <span class="rule"></span></div>
  <p class="lead">God has blessed Meadowlark Fellowship Church with some very gifted people with hearts for service!<br>Here are some ways MFC serves the Lord in ministry.</p>
  <p class="body">The Bible gives a wonderful overview of the process by which the Church grows and matures: It was He who gave some to be apostles, some to be prophets, some to be evangelists, and some to be pastors and teachers, to prepare God's people for works of service, so that the body of Christ may be built up until we all reach unity in the faith and in the knowledge of the Son of God and become mature, attaining to the whole measure of the fullness of Christ.</p>
  <p class="ref">– Ephesians 4:11-13</p>
</section>
<div class="ministry-emblem abs" role="img" aria-label="Circular photo of a church interior framed as a decorative emblem"></div>

<div class="card abs" style="left:60px">
  <div class="card-photo" role="img" aria-label="Photo of a family reading the Bible together" style="background:linear-gradient(135deg,#e8d2b8,#a9876a)"></div>
  <h3>Childrens Ministry</h3>
  <p>We take God's command to teach His truth to children very seriously at MFC, all while the children have a great time! We want kids to LOVE to come to church, too.</p>
  <span class="btn btn-sm">Know More</span>
</div>
<div class="card abs" style="left:420px">
  <div class="card-photo" role="img" aria-label="Photo of a man studying an open Bible" style="background:linear-gradient(135deg,#8a6e55,#3d3026)"></div>
  <h3>Men's Ministry</h3>
  <p>The men's ministry seeks to transform men into committed disciples of Jesus Christ, thereby affecting their families, workplace, church and community.</p>
  <span class="btn btn-sm">Know More</span>
</div>
<div class="card abs" style="left:780px">
  <div class="card-photo" role="img" aria-label="Photo of a woman praying in a sunlit room" style="background:linear-gradient(135deg,#c9a98a,#6e5040)"></div>
  <h3>Women's Ministry</h3>
  <p>Our women's ministry exists to support and encourage women's spiritual growth, to help women get to know one another, and to provide opportunities for women in the community to know</p>
  <span class="btn btn-sm">Know More</span>
</div>

<section class="studies-photo abs" role="img" aria-label="Photo of an oil lamp glowing beside an open Bible"></section>
<div class="studies abs">
  <h2 class="script">Bible Studies</h2>
  <div class="eyebrow">Meadowlark Fellowship Church <span class="rule"></span></div>
  <p class="intro">Each month will bring a new Bible-centered topic covering a broad range of subjects.</p>
  <div class="event">
    <div class="event-date">JAN<b>21</b>WED</div>
    <div class="event-info">
      <h4>Wednesday Night Bible Study</h4>
      <div class="when">Jan 21 @ 7:30 pm – 8:30 pm</div>
      <p>Come join our mid-week Bible Study from 7:30 - 8:30pm<br>Meets at MFC. Contact church office for details.</p>
    </div>
    <div class="event-action"><span class="btn btn-sm">Know More</span></div>
  </div>
  <div class="event">
    <div class="event-date">JAN<b>25</b>SUN</div>
    <div class="event-info">
      <h4>Sunday Service</h4>
      <div class="when">Jan 25 @ 11:00 am – 12:15 pm</div>
      <p>Where is MFC?<br>We are on the northwest corner of Linden Ave</p>
    </div>
    <div class="event-action"><span class="btn btn-sm">Know More</span></div>
  </div>
</div>
<span class="btn abs" style="top:3590px;left:515px">View More</span>

<section class="hope-bg abs" role="img" aria-label="Photo of an open Bible in soft light"></section>
<section class="hope abs">
  <h2>We have this hope as an anchor for the soul,<br>firm and secure. Heb 6:19</h2>
  <div class="eyebrow">If you cannot join us in person</div>
  <span class="btn" style="font-size:18px;padding:18px 42px">Click here for this week's sermon</span>
</section>

<section class="newsletter abs">
  <h2>Sign Up For Our Weekly Newsletter</h2>
  <div class="signup">Enter Your Email Address<span class="btn">Subscribe</span></div>
</section>

<footer class="footer abs">
  <div class="footer-brand abs"><span class="brand-dot"></span>Meadowlark Fellowship Church</div>
  <div class="contacts abs">
    <div class="contact"><span class="icon"><svg width="18" height="18" viewBox="0 0 24 24" fill="#fff"><path d="M6.6 10.8a15 15 0 0 0 6.6 6.6l2.2-2.2a1 1 0 0 1 1-.25 11.4 11.4 0 0 0 3.6.6 1 1 0 0 1 1 1V20a1 1 0 0 1-1 1A17 17 0 0 1 3 4a1 1 0 0 1 1-1h3.5a1 1 0 0 1 1 1c0 1.25.2 2.45.57 3.57a1 1 0 0 1-.25 1z"/></svg></span><span>Call Us<br>(555) 014-2290</span></div>
    <div class="contact"><span class="icon"><svg width="18" height="18" viewBox="0 0 24 24" fill="#fff"><path d="M3 5h18v14H3zM3 5l9 7 9-7" stroke="#0b1b4d" stroke-width="1.5"/></svg></span><span>Mail Us<br>info@meadowlarkfellowship.org</span></div>
    <div class="contact" style="margin-right:160px"><span class="icon"><svg width="18" height="18" viewBox="0 0 24 24" fill="#fff"><path d="M12 2a7 7 0 0 0-7 7c0 5 7 13 7 13s7-8 7-13a7 7 0 0 0-7-7zm0 9.5A2.5 2.5 0 1 1 12 6.5a2.5 2.5 0 0 1 0 5z"/></svg></span><span>2250 Orchard Lane<br>Fairview, California 90000</span></div>
  </div>
  <div class="socials abs"><span class="social"></span><span class="social"></span><span class="social"></span><span class="social"></span></div>
</footer>

<div class="bottom-bar abs">
  <div class="links">HOME | WHO WE ARE | VISITING ON A SUNDAY | KIDS CHURCH | EVENT CALENDAR | OUR MINISTRIES | SUNDAY BIBLE STUDIES | SERMONS | CONTACT US | DONATE</div>
  <div class="legal">Copyright © 2026 All Rights Reserved By Meadowlark Fellowship</div>
  <div class="socials abs"><span class="social"></span><span class="social"></span><span class="social"></span><span class="social"></span></div>
</div>

</body>
</html>
```